Lawyer Needs New Atypical Stationery Design With Gravitas

I need new stationery (letterhead, envelopes, note pads, maybe business cards) for my law office. Although I work by myself, for myself, I need stationery that conveys strength, stability, and gravitas. I would also like a design that makes the end user think: "This is unique. I've never seen letterhead like this before." Most importantly, it should not look like many lawyers' letterhead, meaning no scales of justice. My current letterhead (attached) has my name and "Attorney at Law" on it; however, I would like to transition to "MERIX | LAW" or something like that with the new letterhead. Lastly, I would like an envelope design that is not the standard #10 envelope with a triangular back flap, maybe a square flap or something in the style or design that also makes people stop and think "That's different from anything I've seen before."

```html
<!DOCTYPE html>
<html lang="en">
<head>
<meta charset="utf-8">
<title>MERIX | LAW – Business Card</title>
<link rel="stylesheet" href="https://fonts.googleapis.com/css2?family=Montserrat:wght@400;500&family=Raleway:wght@600&display=swap">
<style>
  :root {
    --page: #ececec;
    --navy: #13284d;
    --paper: #ffffff;
    --ink: #3a3a3a;
    --shadow: rgba(0, 0, 0, 0.12);
  }
  * { box-sizing: border-box; margin: 0; padding: 0; }
  html, body {
    width: 1200px;
    height: 800px;
    overflow: hidden;
    background: var(--page);
  }
  .stage {
    position: relative;
    width: 1200px;
    height: 800px;
  }
  .card {
    position: absolute;
    top: 220px;
    width: 360px;
    height: 360px;
    border-radius: 24px;
    box-shadow: 0 2px 6px var(--shadow);
    overflow: hidden;
  }
  .card--front {
    left: 230px;
    background: var(--paper);
  }
  .card--back {
    left: 620px;
    background: var(--navy);
    display: flex;
    align-items: center;
    justify-content: center;
  }
  .rule {
    position: absolute;
    left: 50%;
    width: 4px;
    margin-left: -2px;
    background: var(--navy);
  }
  .rule--top { top: 0; height: 88px; }
  .rule--bottom { bottom: 0; height: 86px; }
  .contact {
    position: absolute;
    top: 112px;
    left: 0;
    right: 0;
    text-align: center;
  }
  .contact__name {
    font-family: "Raleway", sans-serif;
    font-weight: 600;
    font-size: 19px;
    letter-spacing: 0.3px;
    color: var(--navy);
    margin-bottom: 18px;
  }
  .contact__line {
    font-family: "Montserrat", sans-serif;
    font-weight: 400;
    font-size: 12.5px;
    line-height: 17px;
    color: var(--ink);
  }
  .contact__label {
    font-weight: 500;
    color: var(--navy);
  }
  .contact__address { margin-top: 4px; }
  .wordmark {
    font-family: "Raleway", sans-serif;
    font-weight: 600;
    font-size: 36px;
    letter-spacing: 1px;
    color: var(--paper);
    white-space: nowrap;
  }
</style>
</head>
<body>
  <main class="stage">
    <section class="card card--front" aria-label="Business card front">
      <span class="rule rule--top"></span>
      <div class="contact">
        <h1 class="contact__name">DANIEL MERIX, ESQ.</h1>
        <p class="contact__line"><span class="contact__label">T :</span> (310) 555-0148</p>
        <p class="contact__line"><span class="contact__label">E :</span> Daniel@danielmerix.com</p>
        <p class="contact__line contact__address">4120 Alder Crest Avenue<br>Suite 600 Westbrook,<br>CA 90000-1100</p>
      </div>
      <span class="rule rule--bottom"></span>
    </section>
    <section class="card card--back" aria-label="Business card back">
      <p class="wordmark">MERIX | LAW</p>
    </section>
  </main>
</body>
</html>
```